Banner for my Fitness Clipora channel Marrow Ascent

I need a Banner to be hung in a gym for my fitness Clipora Channel called Marrow Ascent. I was thinking of going with something minmalistic like a Clipora play button and the name of my Clipora Channel next to it.
(Clipora Play Button) | MARROW ASCENT
I also would like to add my motto in this banner which is " STRENGTH . PERFORMANCE . LONGEVITY. "
I would like the emphasis to be on clipora play button and the Marrow Ascent part.
I want something simple but effective that stands out. I will attach a picture of where the banner will be posted so you have a better idea.
My website is www.marrowascent.ca
My Clipora Channel is www.clipora.com/marrowascent
I will attach the location of where the banner will go along with my logo
The size of the banner will be 30 inches in height and 80 inches in length
I am attaching some of my pictures that you may be able to incorporate as a faded background picture . You can either use one or all of them, which ever you feel is best

```html
<!DOCTYPE html>
<html lang="en">
<head>
<meta charset="UTF-8">
<title>Marrow Ascent – Gym Banner</title>
<link href="https://fonts.googleapis.com/css2?family=Roboto:wght@400;500;700;900&display=swap" rel="stylesheet">
<style>
  :root {
    --paper: #ffffff;
    --label: #2b2b2b;
    --ink-light: #ffffff;
    --brand-red: #e02a26;
    --bg-black: #0a0606;
    --bg-deep: #2a0606;
    --bg-red: #8c0f0f;
    --bg-red-hot: #9a1212;
    --bg-edge: #6a0000;
  }
  * { margin: 0; padding: 0; box-sizing: border-box; }
  html, body {
    width: 1200px;
    height: 416px;
    overflow: hidden;
    background: var(--paper);
    font-family: "Roboto", Arial, sans-serif;
  }
  .sheet {
    position: relative;
    width: 1200px;
    height: 416px;
  }
  .dimension {
    position: absolute;
    color: var(--label);
    font-size: 32px;
    font-weight: 400;
    line-height: 1;
  }
  .dimension--width { left: 443px; top: 30px; }
  .dimension--height { left: 1100px; top: 248px; }

  .banner {
    position: absolute;
    left: 0;
    top: 79px;
    width: 1083px;
    height: 337px;
    overflow: hidden;
    color: var(--ink-light);
  }
  .banner__backdrop {
    position: absolute;
    inset: 0;
    background:
      radial-gradient(ellipse 260px 300px at 520px 200px, rgba(150, 20, 20, 0.55), transparent 70%),
      linear-gradient(90deg,
        var(--bg-black) 0%,
        var(--bg-deep) 22%,
        var(--bg-red) 42%,
        var(--bg-red-hot) 58%,
        #4a0303 78%,
        #2a0101 86%,
        var(--bg-edge) 100%);
  }
  .channel {
    position: absolute;
    left: 58px;
    top: 148px;
    display: flex;
    align-items: center;
    gap: 12px;
  }
  .channel__mark {
    width: 44px;
    height: 44px;
    background: var(--brand-red);
  }
  .channel__name {
    font-size: 34px;
    font-weight: 700;
    line-height: 1;
    color: var(--ink-light);
  }
  .divider {
    position: absolute;
    left: 286px;
    top: 104px;
    width: 6px;
    height: 134px;
    background: var(--ink-light);
  }
  .title {
    position: absolute;
    left: 355px;
    top: 137px;
    font-size: 66px;
    font-weight: 900;
    letter-spacing: 3px;
    line-height: 1;
    white-space: nowrap;
  }
  .motto {
    position: absolute;
    left: 298px;
    top: 269px;
    font-size: 16px;
    font-weight: 700;
    letter-spacing: 4.4px;
    line-height: 1;
    white-space: nowrap;
  }
  .website {
    position: absolute;
    left: 439px;
    top: 296px;
    width: 200px;
    text-align: center;
    font-size: 14.5px;
    font-weight: 500;
    letter-spacing: 0.6px;
    line-height: 1.2;
  }
</style>
</head>
<body>
  <div class="sheet">
    <span class="dimension dimension--width">8ft</span>
    <span class="dimension dimension--height">2.5ft</span>

    <section class="banner">
      <div class="banner__backdrop" role="img" aria-label="Faded red-toned photo of an athlete training with cable handles in a gym"></div>

      <div class="channel">
        <span class="channel__mark"></span>
        <span class="channel__name">Clipora</span>
      </div>

      <span class="divider"></span>

      <h1 class="title">MARROW ASCENT</h1>
      <p class="motto">STRENGTH. PERFORMANCE. LONGEVITY.</p>
      <p class="website">www.marrowascent.ca</p>
    </section>
  </div>
</body>
</html>
```